Business Card needed for Drainor, a growing Septic Service company

Drainor, a growing local septic service company in Pennsylvania, needs updated business cards. We'd like the business card to feature our logo and communicate that we provide Septic Pumping, Installations/Repairs, Restroom Rentals, and 24/7 Emergency Service. The business card should be eye-catching, bold, and clean/simple. We have been in business almost 10 years and would like to expand and update our business brand and image.

Target Market(s)

Residential and Commercial, New and Current Homeowners

Industry/Entity Type

Service

Contact Information for Business Card

Contact on the business card should be: Dean Harlow Owner & Operator
Phone: 555-555-0187
Email: service@drainor-example.com
Website: www.drainor-example.com
Address: 812 Millbrook Lane Fernvale ST 00000

Font styles to use
Sans Serif

Colors

Designer to choose colors to be used in the design.

Requirements
Must have
• Feature logo on both side of business card.
Nice to have
• We envision the contact information on one side and our services listed on the other side. Utilize the green from the symbol in our logo as part of the design, overall design color scheme should be white, grey, black.

```html
<!DOCTYPE html>
<html lang="en">
<head>
<meta charset="utf-8">
<title>Drainor Business Card</title>
<link href="https://fonts.googleapis.com/css2?family=Montserrat:wght@400;500;700;800&display=swap" rel="stylesheet">
<style>
  :root {
    --green: #7bbd32;
    --black: #111111;
    --grey-text: #555555;
    --page: #f2f2f2;
    --card: #fafafa;
  }
  * { box-sizing: border-box; margin: 0; padding: 0; }
  html, body { width: 1200px; height: 1200px; overflow: hidden; }
  body {
    background: var(--page);
    font-family: "Montserrat", sans-serif;
    position: relative;
  }
  .card {
    position: absolute;
    left: 150px;
    width: 900px;
    height: 514px;
    background: var(--card);
    border-bottom: 8px solid var(--green);
    box-shadow: 0 10px 24px rgba(0,0,0,0.12);
    overflow: hidden;
  }
  .card--services { top: 70px; }
  .card--contact { top: 616px; }

  .brand {
    position: absolute;
    display: flex;
    align-items: center;
    gap: 16px;
  }
  .brand__square {
    width: 62px;
    height: 62px;
    background: var(--green);
    flex: none;
  }
  .brand__name {
    font-weight: 800;
    font-size: 64px;
    letter-spacing: 2px;
    color: var(--black);
    line-height: 1;
  }
  .brand--stacked {
    flex-direction: column;
    align-items: center;
    gap: 22px;
  }
  .brand--stacked .brand__square { width: 86px; height: 86px; margin-left: 60px; }
  .card--services .brand { left: 120px; top: 215px; }
  .card--contact .brand { left: 70px; top: 380px; }

  .services {
    position: absolute;
    left: 530px;
    top: 110px;
    width: 320px;
  }
  .services__title {
    font-weight: 800;
    font-size: 26px;
    color: var(--black);
    letter-spacing: 0.5px;
    padding-bottom: 10px;
    border-bottom: 1px solid var(--green);
  }
  .services__list {
    list-style: none;
    margin-top: 18px;
    padding-left: 18px;
  }
  .services__item {
    display: flex;
    align-items: center;
    gap: 10px;
    font-size: 17px;
    color: var(--grey-text);
    line-height: 28px;
  }
  .services__item svg { width: 16px; height: 12px; flex: none; }

  .person {
    position: absolute;
    left: 520px;
    top: 70px;
    width: 330px;
  }
  .person__name {
    font-weight: 800;
    font-size: 30px;
    color: var(--green);
    letter-spacing: 0.5px;
  }
  .person__title {
    font-size: 19px;
    color: var(--grey-text);
    padding-bottom: 14px;
    border-bottom: 1px solid var(--green);
  }
  .contact {
    position: absolute;
    left: 540px;
    top: 200px;
    list-style: none;
  }
  .contact__item {
    display: flex;
    align-items: center;
    gap: 12px;
    font-size: 17px;
    color: var(--grey-text);
    line-height: 28px;
  }
  .contact__item--address { align-items: flex-start; margin-bottom: 10px; }
  .contact__item--address svg { margin-top: 16px; }
  .contact__item svg { width: 16px; height: 16px; flex: none; fill: var(--green); }
</style>
</head>
<body>

<section class="card card--services" aria-label="Card front: services">
  <div class="brand brand--stacked">
    <span class="brand__square"></span>
    <span class="brand__name">DRAINOR</span>
  </div>
  <div class="services">
    <h2 class="services__title">SEPTIC SERVICES</h2>
    <ul class="services__list">
      <li class="services__item"><svg viewBox="0 0 16 12"><path d="M1 1l5 5-5 5M8 1l5 5-5 5" stroke="#7bbd32" stroke-width="2.4" fill="none"/></svg>Septic Pumping</li>
      <li class="services__item"><svg viewBox="0 0 16 12"><path d="M1 1l5 5-5 5M8 1l5 5-5 5" stroke="#7bbd32" stroke-width="2.4" fill="none"/></svg>Installations/Repairs</li>
      <li class="services__item"><svg viewBox="0 0 16 12"><path d="M1 1l5 5-5 5M8 1l5 5-5 5" stroke="#7bbd32" stroke-width="2.4" fill="none"/></svg>Restroom Rentals</li>
      <li class="services__item"><svg viewBox="0 0 16 12"><path d="M1 1l5 5-5 5M8 1l5 5-5 5" stroke="#7bbd32" stroke-width="2.4" fill="none"/></svg>24/7 Emergency Service</li>
    </ul>
  </div>
</section>

<section class="card card--contact" aria-label="Card back: contact">
  <div class="person">
    <h2 class="person__name">DEAN HARLOW</h2>
    <p class="person__title">CEO &amp; Founder</p>
  </div>
  <ul class="contact">
    <li class="contact__item contact__item--address">
      <svg viewBox="0 0 16 16"><path d="M8 0a5.5 5.5 0 0 0-5.5 5.5C2.5 10 8 16 8 16s5.5-6 5.5-10.5A5.5 5.5 0 0 0 8 0zm0 8a2.5 2.5 0 1 1 0-5 2.5 2.5 0 0 1 0 5z"/></svg>
      <span>812 Millbrook Lane<br>Fernvale ST 00000</span>
    </li>
    <li class="contact__item">
      <svg viewBox="0 0 16 16"><path d="M3.5 1l2.5 3-1.5 2c1 2 3 4 5 5l2-1.5 3 2.5-1.5 2.5C7 14 2 9 1 2.5z"/></svg>
      <span>555-555-0187</span>
    </li>
    <li class="contact__item">
      <svg viewBox="0 0 16 16"><path d="M1 3h14v1.2L8 9 1 4.2zM1 5.8l7 4.8 7-4.8V13H1z"/></svg>
      <span>service@drainor-example.com</span>
    </li>
    <li class="contact__item">
      <svg viewBox="0 0 16 16"><circle cx="8" cy="8" r="6.5" fill="none" stroke="#7bbd32" stroke-width="1.5"/><path d="M1.5 8h13M8 1.5c-3 3.5-3 9.5 0 13M8 1.5c3 3.5 3 9.5 0 13" fill="none" stroke="#7bbd32" stroke-width="1.2"/></svg>
      <span>www.drainor-example.com</span>
    </li>
  </ul>
  <div class="brand">
    <span class="brand__square"></span>
    <span class="brand__name">DRAINOR</span>
  </div>
</section>

</body>
</html>
```